Northfield Builders Guild Business card

We are looking for a new business card design with photo included.
Our business is a nonprofit construction contractor membership organization. We offer business education, assist with business setup and licensing, provide safety training, and provide a member directory.
URL: www.brickwayguildnetwork.org
Color code:
CMYK: 0 cyan, 42 magenta, 100 yellow, 0 black for Print.
Hexidecimal: #FF9900
RGB: R 255; G 153; B 0

```html
<!DOCTYPE html>
<html lang="en">
<head>
<meta charset="utf-8">
<title>Northfield Builders Guild – Business Card</title>
<link rel="stylesheet" href="https://fonts.googleapis.com/css2?family=Archivo:wght@500;800&display=swap">
<style>
  :root {
    --backdrop: #3a3a3a;
    --card: #ffffff;
    --ink: #2b2b2b;
    --orange: #ff9900;
    --photo-warm: #f3ece0;
    --photo-cool: #e9ebee;
  }
  * { margin: 0; padding: 0; box-sizing: border-box; }
  html, body { width: 1200px; height: 800px; overflow: hidden; }
  body {
    background: radial-gradient(ellipse at 30% 20%, #6b6b6b 0%, var(--backdrop) 55%, #1c1c1c 100%);
    font-family: "Archivo", Arial, sans-serif;
    position: relative;
  }
  .card {
    position: absolute;
    top: 250px;
    width: 525px;
    height: 300px;
    background: var(--card);
    overflow: hidden;
    box-shadow: 0 18px 40px rgba(0,0,0,0.45);
  }
  .card--front { left: 45px; }
  .card--back { left: 630px; }

  .photo { position: absolute; inset: 0; }
  .photo--crew {
    background: linear-gradient(120deg, var(--photo-warm) 0%, #f6f2ea 45%, var(--photo-cool) 100%);
    clip-path: polygon(0 0, 62% 0, 30% 100%, 0 100%);
    opacity: 0.9;
  }
  .photo--tablet {
    background: linear-gradient(200deg, var(--photo-cool) 0%, #eeeeee 60%, #f4f4f4 100%);
    clip-path: polygon(42% 18%, 100% 18%, 100% 100%, 12% 100%, 12% 78%);
    opacity: 0.9;
  }

  .wordmark {
    font-weight: 800;
    color: var(--ink);
    text-transform: uppercase;
    letter-spacing: -0.5px;
    line-height: 0.95;
    display: flex;
    align-items: center;
    gap: 10px;
  }
  .wordmark__mark {
    width: 16px; height: 16px; background: var(--orange); flex: none;
  }
  .card--front .wordmark {
    position: absolute;
    left: 210px; top: 105px;
    font-size: 38px;
  }
  .card--front .wordmark__name { display: block; }

  .card--back .wordmark {
    position: absolute;
    left: 34px; top: 40px;
    font-size: 26px;
  }
  .rule {
    position: absolute;
    left: 34px; right: 34px; top: 86px;
    height: 1.5px;
    background: var(--orange);
  }
  .contact {
    position: absolute;
    left: 34px; top: 110px;
    list-style: none;
    font-weight: 500;
    font-size: 12.5px;
    color: var(--ink);
    line-height: 1.5;
  }
  .contact li { display: flex; align-items: flex-start; gap: 10px; }
  .contact svg { width: 12px; height: 12px; margin-top: 3px; flex: none; }
</style>
</head>
<body>

<section class="card card--front" aria-label="Card front">
  <div class="photo photo--crew" role="img" aria-label="Faded photo of two construction workers in hard hats and safety vests reviewing plans"></div>
  <div class="wordmark">
    <span class="wordmark__mark"></span>
    <span class="wordmark__name">Northfield<br>Builders<br>Guild</span>
  </div>
</section>

<section class="card card--back" aria-label="Card back">
  <div class="photo photo--tablet" role="img" aria-label="Faded photo of a gloved hand holding a smartphone at a job site"></div>
  <div class="wordmark">
    <span class="wordmark__mark"></span>
    <span class="wordmark__name">Northfield Builders Guild</span>
  </div>
  <div class="rule"></div>
  <ul class="contact">
    <li>
      <svg viewBox="0 0 12 12" fill="none" stroke="#ff9900" stroke-width="1.2"><path d="M6 11s4-4 4-6.5A4 4 0 0 0 2 4.5C2 7 6 11 6 11z"/><circle cx="6" cy="4.5" r="1.3"/></svg>
      <span>4820 Larkspur Ave, Suite 210<br>Millbrook, OR 97308</span>
    </li>
    <li>
      <svg viewBox="0 0 12 12" fill="none" stroke="#ff9900" stroke-width="1.1"><circle cx="6" cy="6" r="5"/><path d="M1 6h10M6 1c2 2 2 8 0 10M6 1c-2 2-2 8 0 10"/></svg>
      <span>www.brickwayguildnetwork.org</span>
    </li>
    <li>
      <svg viewBox="0 0 12 12" fill="none" stroke="#ff9900" stroke-width="1.2"><path d="M2.5 1.5l2 .5.7 2.2-1.2 1a6 6 0 0 0 2.8 2.8l1-1.2 2.2.7.5 2c-4.5.8-8.8-3.5-8-8z"/></svg>
      <span>(555) 318-2740</span>
    </li>
    <li>
      <svg viewBox="0 0 12 12" fill="none" stroke="#ff9900" stroke-width="1.1"><rect x="1.5" y="4" width="9" height="6.5"/><path d="M3.5 4V1.5h5V4M3.5 7h5"/></svg>
      <span>555.604.1193</span>
    </li>
    <li>
      <svg viewBox="0 0 12 12" fill="none" stroke="#ff9900" stroke-width="1.1"><rect x="1" y="2.5" width="10" height="7"/><path d="M1 2.5l5 4 5-4"/></svg>
      <span>support@nbguild.org</span>
    </li>
  </ul>
</section>

</body>
</html>
```